Oil & gas fabrication and Paint company. Need double sided with color. want original look. see attached but don't make similar!

Think Steel!

Business

```html
<!DOCTYPE html>
<html lang="en">
<head>
<meta charset="utf-8">
<title>Keelson Fabrication &amp; Paint — Business Card</title>
<link rel="stylesheet" href="https://fonts.googleapis.com/css2?family=Bitter:wght@400;700&family=Open+Sans:wght@400;600&display=swap">
<style>
  :root {
    --navy: #1c1f78;
    --navy-deep: #121452;
    --navy-light: #2d3299;
    --ink: #222326;
    --rule: #c9c9cc;
    --paper: #ffffff;
    --stage: #ecebe8;
    --steel-dark: #1a1a1a;
    --steel-light: #e6e6e6;
    --gold: #f2b21c;
  }
  html, body {
    margin: 0;
    width: 1200px;
    height: 549px;
    overflow: hidden;
    background: var(--stage);
  }
  .sheet {
    position: relative;
    width: 1200px;
    height: 549px;
  }
  .card {
    position: absolute;
    top: 124px;
    width: 520px;
    height: 300px;
    overflow: hidden;
    box-shadow: 0 6px 18px rgba(0,0,0,.18);
  }
  /* Front */
  .card-front { left: 40px; background: var(--paper); }
  .brand {
    position: absolute;
    left: 32px;
    top: 92px;
    width: 210px;
    display: flex;
    align-items: center;
    gap: 10px;
  }
  .brand-dot {
    width: 22px; height: 22px;
    border-radius: 50%;
    background: var(--navy);
    flex: none;
  }
  .brand-name {
    font-family: "Bitter", serif;
    font-weight: 700;
    font-size: 38px;
    letter-spacing: 2px;
    color: var(--navy);
  }
  .brand-tag {
    position: absolute;
    left: 64px;
    top: 142px;
    font-family: "Bitter", serif;
    font-size: 13px;
    color: var(--navy);
  }
  .divider {
    position: absolute;
    left: 262px;
    top: 90px;
    width: 1px;
    height: 120px;
    background: var(--rule);
  }
  .contact {
    position: absolute;
    left: 276px;
    top: 40px;
    font-family: "Bitter", serif;
    font-size: 14px;
    color: var(--ink);
    line-height: 20px;
  }
  .address { margin: 0 0 14px; }
  .contact-list { list-style: none; margin: 0; padding: 0 0 0 10px; }
  .contact-list li { display: flex; align-items: center; gap: 7px; }
  .contact-list svg { width: 12px; height: 12px; fill: var(--ink); flex: none; }
  .band { position: absolute; left: 0; top: 0; width: 520px; height: 300px; }
  .holder-name {
    position: absolute;
    right: 44px;
    top: 250px;
    font-family: "Bitter", serif;
    font-weight: 700;
    font-size: 20px;
    color: var(--paper);
  }
  /* Back */
  .card-back { left: 640px; }
  .back-texture {
    position: absolute; inset: 0;
    background: radial-gradient(ellipse at 50% 40%, var(--navy-light), var(--navy) 55%, var(--navy-deep));
  }
  .back-brand {
    position: absolute;
    left: 0; right: 0;
    top: 104px;
    text-align: center;
    font-family: "Bitter", serif;
    font-weight: 700;
    font-size: 60px;
    letter-spacing: 4px;
    color: var(--paper);
  }
  .back-tag {
    position: absolute;
    left: 0; right: 0;
    top: 180px;
    text-align: center;
    font-family: "Bitter", serif;
    font-size: 17px;
    color: var(--paper);
  }
  .back-web {
    position: absolute;
    left: 0; right: 0;
    top: 236px;
    text-align: center;
    font-family: "Open Sans", sans-serif;
    font-size: 19px;
    color: var(--paper);
    letter-spacing: .5px;
  }
</style>
</head>
<body>
<main class="sheet">

  <section class="card card-front">
    <svg class="band" viewBox="0 0 520 300" aria-hidden="true">
      <defs>
        <linearGradient id="steelFade" x1="0" x2="1">
          <stop offset="0" stop-color="var(--steel-light)"/>
          <stop offset="1" stop-color="var(--steel-dark)"/>
        </linearGradient>
      </defs>
      <polygon points="0,270 246,270 236,282 0,288" fill="url(#steelFade)"/>
      <polygon points="0,290 262,280 290,242 520,242 520,300 0,300" fill="var(--navy)"/>
    </svg>

    <div class="brand">
      <span class="brand-dot"></span>
      <span class="brand-name">KEELSON</span>
    </div>
    <div class="brand-tag">Fabrication &amp; Paint</div>

    <div class="divider"></div>

    <div class="contact">
      <p class="address">4820 County Road 12<br>Conroe, TX 77301</p>
      <ul class="contact-list">
        <li><svg viewBox="0 0 12 12"><path d="M2.5 1h2l1 3-1.3 1a6 6 0 0 0 2.8 2.8L8 6.5l3 1v2A1.5 1.5 0 0 1 9.5 11 8.5 8.5 0 0 1 1 2.5 1.5 1.5 0 0 1 2.5 1z"/></svg>281-555-0142</li>
        <li><svg viewBox="0 0 12 12"><path d="M3 1h6v3H3zM1 5h10v5H1zM3 8h6v3H3z"/></svg>1-888-555-0176</li>
        <li><svg viewBox="0 0 12 12"><path d="M2.5 1h2l1 3-1.3 1a6 6 0 0 0 2.8 2.8L8 6.5l3 1v2A1.5 1.5 0 0 1 9.5 11 8.5 8.5 0 0 1 1 2.5 1.5 1.5 0 0 1 2.5 1z"/></svg>1-888-5-STEEL</li>
        <li><svg viewBox="0 0 12 12"><path d="M1 3h10v7H1zM1 3l5 4 5-4" stroke="#fff" stroke-width=".8"/></svg>dale@keelsonworks.net</li>
        <li><svg viewBox="0 0 12 12"><circle cx="6" cy="6" r="5"/><path d="M1 6h10M6 1c-2 3-2 7 0 10M6 1c2 3 2 7 0 10" stroke="#fff" stroke-width=".8" fill="none"/></svg>www.keelsonworks.net</li>
      </ul>
    </div>

    <div class="holder-name">Dale Marrow</div>
  </section>

  <section class="card card-back">
    <div class="back-texture" role="img" aria-label="Fine hexagon steel-mesh texture in deep navy"></div>
    <div class="back-brand">KEELSON</div>
    <div class="back-tag">Fabrication &amp; Paint</div>
    <div class="back-web">www.keelsonworks.net</div>
  </section>

</main>
</body>
</html>
```